Creative Swimming Pool Facebook Design

We need A creative Facebook Page for a swimming pool company named "Brimwell Pools" using our logo. Our slogan is "better service for a better price." the design should have a Connecticut feel to it (not tropics).

Industry/Entity Type

It Company

Font styles to use
Serif
Sans Serif

```html
<!DOCTYPE html>
<html lang="en">
<head>
<meta charset="utf-8">
<title>Brimwell Pools – Page</title>
<link rel="stylesheet" href="https://fonts.googleapis.com/css2?family=Arimo:wght@400;700&family=Lato:wght@400&display=swap">
<style>
:root{
  --page-bg:#e9eaed;
  --bar-blue:#3b5998;
  --bar-blue-top:#4e69a2;
  --sub-bar:#6d84b4;
  --panel:#ffffff;
  --line:#dddfe2;
  --text:#1d2129;
  --muted:#4b4f56;
  --grey:#90949c;
  --link:#3b5998;
  --brand-blue:#2a9fd6;
  --slogan:#c9c9c9;
  --button-bg:#f6f7f9;
  --post-blue:#4e69a2;
  --avatar:#c5cbd8;
}
*{box-sizing:border-box;margin:0;padding:0}
html,body{width:1200px;height:893px;overflow:hidden;background:var(--page-bg)}
body{font-family:"Arimo",Helvetica,Arial,sans-serif;color:var(--text)}
.stage{position:relative;width:1122px;height:835px;transform:scale(1.0695);transform-origin:0 0}
.abs{position:absolute}

.top-bar{left:0;top:0;width:1122px;height:43px;background:linear-gradient(var(--bar-blue-top),var(--bar-blue));border-bottom:1px solid #29487d}
.top-bar .mark{left:75px;top:9px;width:22px;height:22px;background:#fff;border-radius:2px}
.search{left:105px;top:9px;width:400px;height:24px;background:#fff;border-radius:2px;font-size:14px;color:#666;padding:4px 7px;line-height:16px}
.search svg{position:absolute;right:0;top:0}
.notice-bar{left:0;top:43px;width:1122px;height:27px;background:var(--sub-bar);color:#eef1f7;font-size:12px;text-align:center;line-height:26px}
.notice-bar b{font-weight:700;color:#fff}

.page-nav{left:75px;top:70px;width:984px;height:45px;background:var(--panel);border:1px solid var(--line);border-top:0;border-radius:0 0 3px 3px}
.page-nav a{position:absolute;top:0;height:45px;line-height:45px;font-size:14px;color:var(--muted);text-decoration:none}
.page-nav .current{font-weight:700;color:var(--text);border-bottom:3px solid #4267b2;line-height:46px}
.page-nav .sep{position:absolute;top:10px;width:1px;height:26px;background:var(--line)}

.cover-water{left:75px;top:124px;width:460px;height:315px;background:radial-gradient(ellipse at 30% 40%,#7ed3f5,#1e9fe0 45%,#0d6fbd 100%)}
.cover-wood{left:535px;top:124px;width:390px;height:315px;background:linear-gradient(90deg,#3a3837,#2c2b2a 30%,#3b3938 55%,#2b2a29 80%,#363433)}
.wordmark{left:535px;top:250px;width:390px;display:flex;justify-content:center;align-items:center;gap:12px}
.wordmark .dot{width:18px;height:18px;border-radius:50%;background:var(--brand-blue)}
.wordmark .name{font-family:"Lato",Arial,sans-serif;font-weight:400;font-size:34px;line-height:40px;color:var(--brand-blue)}
.slogan{left:535px;top:304px;width:390px;text-align:center;font-family:"Lato",Arial,sans-serif;font-weight:400;font-size:18px;line-height:22px;color:var(--slogan);letter-spacing:.5px}

.profile-pic{left:90px;top:301px;width:168px;height:168px;background:#fff;border:1px solid #ccc;padding:4px;border-radius:2px}
.profile-pic div{width:100%;height:100%;background:radial-gradient(ellipse at 40% 40%,#6ecbf2,#1a98dc 55%,#0e72bf)}
.page-title{left:269px;top:369px;color:#fff;font-size:23px;font-weight:700;text-shadow:0 0 3px rgba(0,0,0,.5)}
.page-type{left:269px;top:402px;color:#fff;font-size:17px;text-shadow:0 0 3px rgba(0,0,0,.5)}

.btn{position:absolute;height:25px;background:var(--button-bg);border:1px solid #cdd0d6;border-radius:2px;font-size:12px;font-weight:700;color:var(--muted);line-height:23px;display:flex;align-items:center;gap:5px;padding:0 8px;white-space:nowrap}
.btn.liked{left:600px;top:400px;width:84px;color:#4267b2}
.btn-group{left:695px;top:400px;width:218px;height:25px}
.btn-group .btn{top:0}

.tab-bar{left:75px;top:439px;width:850px;height:43px;background:var(--panel);border:1px solid var(--line);border-top:0}
.tab-bar a{position:absolute;top:0;line-height:42px;font-size:14px;color:var(--muted);text-decoration:none}
.tab-bar .current{font-weight:700;color:var(--text);border-bottom:3px solid #4e69a2;line-height:43px}
.tab-bar .sep{position:absolute;top:10px;width:1px;height:24px;background:var(--line)}

.stats{left:937px;top:125px;width:122px;height:291px;background:var(--panel);border:1px solid var(--line)}
.stats .head{height:37px;line-height:36px;text-align:center;font-size:12px;font-weight:700;background:#f6f7f9;border-bottom:1px solid var(--line)}
.stats .item{margin:0 10px;height:54px;text-align:center;padding-top:12px;border-bottom:1px solid var(--line)}
.stats .item:last-child{border-bottom:0}
.stats .num{font-size:13px;font-weight:700}
.stats .label{font-size:11px;color:var(--link)}
.stats .head.alt{border-top:1px solid var(--line)}

.years{left:937px;top:437px;border-left:4px solid #cdd0d6;font-size:12px;color:#9197a3}
.years li{list-style:none;padding:4px 0 2px 10px;height:24px}
.years .on{font-weight:700;color:#7f7f7f;border-left:4px solid #6e7b91;margin-left:-4px}

.people{left:75px;top:494px;width:329px;height:312px;background:var(--panel);border:1px solid var(--line);border-radius:3px}
.people .head{height:37px;line-height:36px;padding-left:11px;font-size:11px;font-weight:700;color:var(--muted);background:#f6f7f9;border-bottom:1px solid var(--line);position:relative}
.people .head svg{position:absolute;right:10px;top:12px}
.people .count{text-align:center;font-size:14px;padding:13px 0;border-bottom:1px solid var(--line);color:var(--grey)}
.people .count b{color:var(--text)}
.people .likers{font-size:12px;color:var(--muted);padding:13px 13px 8px}
.people a{color:var(--link);font-weight:700;text-decoration:none}
.avatar{background:var(--avatar);width:45px;height:45px;position:absolute}
.more-count{background:#dfe3ee;color:var(--post-blue);font-weight:700;font-size:18px;text-align:center;line-height:45px}
.invite-row{position:absolute;left:88px;width:303px;height:40px}
.invite-row .name{position:absolute;left:48px;top:13px;font-size:12px;font-weight:700;color:var(--link)}
.invite-row .btn{right:0;top:8px;height:24px;font-size:12px}
.see-all{position:absolute;left:88px;top:779px;font-size:12px;color:var(--link)}

.composer{left:415px;top:494px;width:510px;height:312px;background:var(--panel);border:1px solid var(--line);border-radius:3px}
.composer .tabs{height:35px;border-bottom:1px solid var(--line);font-size:12px;font-weight:700;color:var(--muted);position:relative}
.composer .tabs span{position:absolute;top:10px;display:flex;align-items:center;gap:6px}
.composer .body{position:absolute;left:64px;top:47px;width:432px;font-size:13.5px;line-height:18.2px;color:var(--text);height:218px;overflow:hidden}
.composer .foot{position:absolute;left:0;bottom:0;width:100%;height:43px;background:#f6f7f9;border-top:1px solid var(--line)}
.post-btn{position:absolute;right:8px;top:7px;width:60px;height:25px;background:var(--post-blue);color:#fff;font-size:12px;font-weight:700;text-align:center;line-height:25px;border-radius:2px}
</style>
</head>
<body>
<div class="stage">

  <header class="top-bar abs">
    <div class="mark abs"></div>
    <div class="search abs">Search for people, places and things
      <svg width="26" height="24" viewBox="0 0 26 24"><line x1="0.5" y1="0" x2="0.5" y2="24" stroke="#ddd"/><circle cx="12" cy="11" r="4.5" fill="none" stroke="#9aa" stroke-width="1.6"/><line x1="15" y1="14" x2="19" y2="18" stroke="#9aa" stroke-width="1.8"/></svg>
    </div>
  </header>
  <div class="notice-bar abs">You are posting, commenting and liking as <b>Your Page Name</b> — Change to Personal Profile</div>

  <nav class="page-nav abs">
    <a class="current" style="left:16px">Page</a>
    <span class="sep" style="left:69px"></span>
    <a style="left:85px">Activity</a>
    <span class="sep" style="left:145px"></span>
    <a style="left:162px">Insights</a>
    <span class="sep" style="left:228px"></span>
    <a style="left:245px">Settings</a>
    <a style="left:781px">Build Audience ▾</a>
    <span class="sep" style="left:906px"></span>
    <a style="left:923px">Help ▾</a>
  </nav>

  <div class="cover-water abs" role="img" aria-label="Rippling swimming pool water"></div>
  <div class="cover-wood abs" role="img" aria-label="Dark weathered wooden boards"></div>
  <div class="wordmark abs"><span class="dot"></span><span class="name">Brimwell Pools</span></div>
  <div class="slogan abs">“BETTER SERVICE FOR<br>A BETTER PRICE”</div>

  <div class="profile-pic abs"><div role="img" aria-label="Pool water profile picture"></div></div>
  <div class="page-title abs">BRIMWELL POOLS</div>
  <div class="page-type abs">Swimming Pool Company</div>

  <div class="btn liked"><svg width="12" height="12" viewBox="0 0 12 12"><path d="M1 5h2v6H1zM4 5l3-4c1 0 1.5.6 1.3 1.6L8 4.5h2.5c.8 0 1.3.7 1 1.4l-1.3 4.4c-.2.5-.6.7-1 .7H4z" fill="#4267b2"/></svg>Liked ▾</div>
  <div class="btn-group abs">
    <div class="btn" style="left:0;width:90px"><svg width="11" height="10" viewBox="0 0 11 10"><path d="M1 5l3 3 6-7" fill="none" stroke="#4b4f56" stroke-width="2"/></svg>Following</div>
    <div class="btn" style="left:89px;width:89px"><svg width="12" height="11" viewBox="0 0 12 11"><path d="M0 0h12v8H5l-3 3V8H0z" fill="#4b4f56"/></svg>Message</div>
    <div class="btn" style="left:177px;width:41px;justify-content:center;font-size:16px;letter-spacing:1px">•••</div>
  </div>

  <nav class="tab-bar abs">
    <span class="sep" style="left:183px"></span>
    <a class="current" style="left:200px">Timeline</a>
    <span class="sep" style="left:277px"></span>
    <a style="left:292px">About</a>
    <span class="sep" style="left:345px"></span>
    <a style="left:362px">Photos</a>
    <span class="sep" style="left:422px"></span>
    <a style="left:439px">Likes</a>
    <span class="sep" style="left:488px"></span>
    <a style="left:505px">More ▾</a>
  </nav>

  <aside class="stats abs">
    <div class="head">THIS WEEK</div>
    <div class="item"><div class="num">999</div><div class="label">Page Likes</div></div>
    <div class="item"><div class="num">999</div><div class="label">Post Reach</div></div>
    <div class="head alt">UNREAD</div>
    <div class="item"><div class="num">999</div><div class="label">Notifications</div></div>
    <div class="item"><div class="num">999</div><div class="label">Messages</div></div>
  </aside>

  <ul class="years abs">
    <li class="on">Recent</li><li>2013</li><li>2012</li><li>2011</li><li>2010</li>
  </ul>

  <section class="people abs">
    <div class="head">PEOPLE<svg width="8" height="12" viewBox="0 0 8 12"><path d="M1 1l5 5-5 5" fill="none" stroke="#4b4f56" stroke-width="2"/></svg></div>
    <div class="count"><b>999</b> likes</div>
    <div class="likers"><a>Example person</a>, and <a>99 others</a> like this.</div>
  </section>
  <div class="avatar" style="left:88px;top:615px"></div>
  <div class="avatar" style="left:138px;top:615px"></div>
  <div class="avatar" style="left:188px;top:615px"></div>
  <div class="avatar" style="left:238px;top:615px"></div>
  <div class="avatar" style="left:288px;top:615px"></div>
  <div class="avatar more-count" style="left:338px;top:615px">+99</div>
  <div class="invite-row" style="top:672px"><div class="avatar" style="left:0;top:0;width:40px;height:40px"></div><span class="name">Example person</span><div class="btn">Invite</div></div>
  <div class="invite-row" style="top:723px"><div class="avatar" style="left:0;top:0;width:40px;height:40px"></div><span class="name">Example person</span><div class="btn">Invite</div></div>
  <div class="see-all">See All Friends</div>

  <section class="composer abs">
    <div class="tabs">
      <span style="left:12px"><svg width="14" height="14"><rect width="14" height="14" rx="2" fill="#4e69a2"/><path d="M4 10l1-3 4-4 2 2-4 4z" fill="#fff"/></svg>Status</span>
      <span style="left:91px"><svg width="14" height="14"><rect x="1" y="1" width="12" height="12" fill="none" stroke="#e98b39" stroke-width="2"/><rect x="4" y="4" width="6" height="6" fill="#e98b39"/></svg>Photo / Video</span>
      <span style="left:207px"><svg width="14" height="14"><rect x="0.5" y="0.5" width="13" height="13" fill="#fff" stroke="#666"/><rect x="0.5" y="0.5" width="13" height="3" fill="#666"/><text x="7" y="12" font-size="7" text-anchor="middle" fill="#333">31</text></svg>Event, Milestone +</span>
    </div>
    <div class="avatar" style="left:11px;top:48px;width:40px;height:38px"></div>
    <p class="body">Lorem ipsum dolor sit amet, consectetur adipiscing elit. Etiam sit amet ante nisi, sit amet fermentum erat. Suspendisse vel nunc a massa consequat iaculis. Sed pellentesque vehicula elit. Mauris sodales mollis molestie. Integer ultrices laoreet ante, et faucibus sem cursus non. Suspendisse laoreet suscipit vestibulum. Integer mi augue, hendrerit ut fermentum ut, accumsan eget justo. Nam fringilla dapibus risus sed consequat. Nullam lacus urna, pellentesque et laoreet sit amet, volutpat sit amet dolor. Praesent a ultrices velit. Nulla facilisi. Ut sagittis dapibus bibendum. Proin id enim eros. Curabitur tincidunt lorem sed purus semper vitae tincidunt purus aliquet. Integer nulla metus, vestibulum at tincidunt at, euismod sed ligula. Vestibulum ante ipsum primis in faucibus orci</p>
    <div class="foot">
      <svg style="position:absolute;left:12px;top:13px" width="16" height="16"><circle cx="8" cy="8" r="7" fill="none" stroke="#90949c" stroke-width="1.6"/><path d="M8 4v4h3" fill="none" stroke="#90949c" stroke-width="1.6"/></svg>
      <svg style="position:absolute;left:53px;top:12px" width="12" height="17"><path d="M6 16C2 10 1 8 1 6a5 5 0 0 1 10 0c0 2-1 4-5 10z" fill="#90949c"/><circle cx="6" cy="6" r="2" fill="#f6f7f9"/></svg>
      <svg style="position:absolute;left:91px;top:14px" width="17" height="14"><rect x="0" y="3" width="17" height="11" rx="2" fill="#90949c"/><rect x="5" y="0" width="7" height="4" fill="#90949c"/><circle cx="8.5" cy="8.5" r="3" fill="#f6f7f9"/></svg>
      <div class="btn" style="left:333px;top:8px;width:93px;justify-content:center">Boost Post ▾</div>
      <div class="post-btn">Post</div>
    </div>
  </section>

</div>
</body>
</html>
```